Process Graphic for website

We would like to design a graphic that shows our internal process for scanning our customer records. Our process is listed in order below:
Transport Documents
Inventory Records
Document Preparation
Scan Documents
AI & Data Extraction
Quality Control
Deliver Documents
Records Retention or Destruction

Our customers need to know that we have a clear defined process for scanning records and it needs to visually demonstrate that in a simple way. I have attached our logo as these are the colors of our new website so whatever colors you chose should match our site.

```html
<!DOCTYPE html>
<html lang="en">
<head>
<meta charset="utf-8">
<title>Our Process</title>
<link rel="stylesheet" href="https://fonts.googleapis.com/css2?family=Poppins:wght@400;500;600;700&family=Oswald:wght@300;400;500&display=swap">
<style>
:root{
  --navy:#2e3192;
  --gold:#d09e1a;
  --page-gray:#eeeef0;
  --panel-gray:#f4f4f6;
  --white:#ffffff;
  --text-dark:#333333;
}
html,body{margin:0;padding:0;overflow:hidden;background:var(--white);}
.canvas{width:716px;height:1200px;overflow:hidden;position:relative;background:var(--white);}
.stage{position:absolute;left:0;top:0;width:904px;height:1530px;transform:scale(0.792,0.7843);transform-origin:0 0;}
.stage svg{position:absolute;left:0;top:0;}
.brand{font-family:"Poppins",sans-serif;font-weight:600;fill:var(--navy);}
.label-sm{font-family:"Poppins",sans-serif;font-size:9px;font-weight:500;fill:var(--white);}
.label-cond{font-family:"Oswald",sans-serif;font-weight:300;font-size:17px;fill:var(--white);}
.label-card{font-family:"Poppins",sans-serif;font-weight:600;font-size:13px;fill:var(--text-dark);}
.num{font-family:"Oswald",sans-serif;font-weight:500;font-size:13px;fill:var(--white);}
.num-card{font-family:"Poppins",sans-serif;font-weight:600;font-size:13px;fill:var(--navy);}
.ico{fill:none;stroke:var(--navy);stroke-width:1.6;stroke-linecap:round;stroke-linejoin:round;}
.ico .g{stroke:var(--gold);}
.card{fill:var(--white);}
.link{fill:none;stroke:var(--gold);stroke-width:1.2;}
</style>
</head>
<body>
<div class="canvas">
<div class="stage">
<svg width="904" height="1530" viewBox="0 0 904 1530" xmlns="http://www.w3.org/2000/svg">
  <defs>
    <symbol id="i-transport" viewBox="0 0 40 40"><g class="ico"><circle cx="20" cy="20" r="7"/><path d="M20 8v3M20 29v3M8 20h3M29 20h3M11.5 11.5l2 2M26.5 26.5l2 2M11.5 28.5l2-2M26.5 13.5l2-2"/><circle cx="20" cy="20" r="3"/><path class="g" d="M5 20a15 15 0 0 1 25-11M35 20a15 15 0 0 1-25 11"/></g></symbol>
    <symbol id="i-inventory" viewBox="0 0 40 40"><g class="ico"><rect x="8" y="7" width="20" height="28" rx="2"/><rect x="13" y="4" width="10" height="5" rx="1"/><path d="M12 15h2M17 15h7M12 20h2M17 20h7M12 25h2M17 25h5"/><circle class="g" cx="31" cy="27" r="4"/></g></symbol>
    <symbol id="i-prep" viewBox="0 0 40 40"><g class="ico"><path d="M10 5h16l5 5v22H10z"/><path d="M14 35h20V12"/><circle class="g" cx="20" cy="15" r="5"/><path class="g" d="M17.5 15l2 2 3.5-4"/><path d="M14 24h13M14 28h10"/></g></symbol>
    <symbol id="i-scan" viewBox="0 0 40 40"><g class="ico"><path d="M4 11V5h6M30 5h6v6M36 29v6h-6M10 35H4v-6"/><path d="M13 10h10l4 4v16H13z"/><path class="g" d="M8 20h24"/><path d="M16 16h6M16 25h8"/></g></symbol>
    <symbol id="i-ai" viewBox="0 0 40 40"><g class="ico"><path class="g" d="M10 16a6 6 0 0 1 6-8 7 7 0 0 1 12 2 5 5 0 0 1 2 9"/><circle cx="20" cy="21" r="6"/><circle cx="20" cy="21" r="2.5"/><path d="M20 13v2M20 27v2M12 21h2M26 21h2"/><path d="M8 36V26M5 29l3-3 3 3M32 25v10M29 32l3 3 3-3"/></g></symbol>
    <symbol id="i-quality" viewBox="0 0 40 40"><g class="ico"><circle cx="14" cy="16" r="9"/><circle class="g" cx="14" cy="16" r="5"/><path d="M14 25v11"/><rect x="27" y="6" width="4" height="4"/><rect x="33" y="6" width="4" height="4"/><rect x="27" y="13" width="4" height="4"/><rect x="27" y="22" width="4" height="4"/><rect x="33" y="22" width="4" height="4"/></g></symbol>
    <symbol id="i-deliver" viewBox="0 0 40 40"><g class="ico"><path d="M20 6a14 14 0 0 0 0 28"/><path d="M20 12a8 8 0 0 0 0 16"/><path d="M11 8l2 2M6 20h3M11 32l2-2M20 4v3M20 33v3"/><path class="g" d="M20 14h8l3-3M20 20h12M20 26h8l3 3"/><circle class="g" cx="33" cy="10" r="1.5"/><circle class="g" cx="34" cy="20" r="1.5"/><circle class="g" cx="33" cy="30" r="1.5"/></g></symbol>
    <symbol id="i-records" viewBox="0 0 40 40"><g class="ico"><path d="M6 14h16v20H10l-4-4z"/><rect x="12" y="19" width="4" height="4"/><rect class="g" x="22" y="6" width="5" height="5"/><rect class="g" x="30" y="6" width="5" height="5"/><rect x="22" y="14" width="5" height="5"/><rect class="g" x="30" y="14" width="5" height="5"/></g></symbol>
  </defs>

  <!-- page backdrop -->
  <rect x="0" y="0" width="904" height="882" fill="var(--page-gray)"/>

  <!-- ===== Panel 1: horizontal strip ===== -->
  <g class="panel-strip">
    <rect x="31" y="30" width="842" height="298" fill="var(--white)"/>
    <text x="89" y="88" font-family="Poppins, sans-serif" font-weight="700" font-size="19"><tspan fill="var(--navy)">OUR </tspan><tspan fill="var(--gold)">PROCESS</tspan></text>
    <rect x="688" y="81" width="9" height="9" fill="var(--navy)"/>
    <text class="brand" x="703" y="93" font-size="22">Northvale</text>

    <g class="strip-links">
      <path class="link" d="M76 214L66 268H130"/>
      <path class="link" d="M174 214L164 268H228"/>
      <path class="link" d="M271 214L261 268H325"/>
      <path class="link" d="M369 214L359 268H423"/>
      <path class="link" d="M467 214L457 268H521"/>
      <path class="link" d="M564 214L554 268H618"/>
      <path class="link" d="M662 214L652 268H716"/>
      <path class="link" d="M760 214L750 268H814"/>
    </g>

    <g class="strip-steps">
      <polygon points="78,209 150,209 144,264 72,264" fill="var(--navy)"/>
      <polygon points="176,209 248,209 242,264 170,264" fill="var(--navy)"/>
      <polygon points="273,209 345,209 339,264 267,264" fill="var(--navy)"/>
      <polygon points="371,209 443,209 437,264 365,264" fill="var(--navy)"/>
      <polygon points="469,209 541,209 535,264 463,264" fill="var(--navy)"/>
      <polygon points="566,209 638,209 632,264 560,264" fill="var(--navy)"/>
      <polygon points="664,209 736,209 730,264 658,264" fill="var(--navy)"/>
      <polygon points="762,209 834,209 828,264 756,264" fill="var(--navy)"/>

      <text class="label-sm" text-anchor="middle"><tspan x="111" y="235">Transport</tspan><tspan x="111" y="246">Documents</tspan></text>
      <text class="label-sm" text-anchor="middle"><tspan x="209" y="235">Inventory</tspan><tspan x="209" y="246">Records</tspan></text>
      <text class="label-sm" text-anchor="middle"><tspan x="306" y="235">Document</tspan><tspan x="306" y="246">Preparation</tspan></text>
      <text class="label-sm" text-anchor="middle"><tspan x="404" y="235">Scan</tspan><tspan x="404" y="246">Documents</tspan></text>
      <text class="label-sm" text-anchor="middle"><tspan x="502" y="235">AI &amp; Data</tspan><tspan x="502" y="246">Extraction</tspan></text>
      <text class="label-sm" text-anchor="middle"><tspan x="599" y="235">Quality</tspan><tspan x="599" y="246">Control</tspan></text>
      <text class="label-sm" text-anchor="middle"><tspan x="697" y="235">Deliver</tspan><tspan x="697" y="246">Documents</tspan></text>
      <text class="label-sm" text-anchor="middle"><tspan x="795" y="228">Records</tspan><tspan x="795" y="239">Retention or</tspan><tspan x="795" y="250">Destruction</tspan></text>

      <use href="#i-transport" x="106" y="170" width="28" height="28"/>
      <use href="#i-inventory" x="201" y="170" width="28" height="28"/>
      <use href="#i-prep" x="299" y="170" width="28" height="28"/>
      <use href="#i-scan" x="396" y="170" width="28" height="28"/>
      <use href="#i-ai" x="491" y="170" width="28" height="28"/>
      <use href="#i-quality" x="592" y="170" width="28" height="28"/>
      <use href="#i-deliver" x="688" y="170" width="28" height="28"/>
      <use href="#i-records" x="789" y="170" width="28" height="28"/>
    </g>
  </g>

  <!-- ===== Panel 2: timeline ===== -->
  <g class="panel-timeline">
    <rect x="31" y="350" width="842" height="510" fill="var(--white)"/>
    <polygon points="31,350 627,350 614,414 31,414" fill="var(--navy)"/>
    <polygon points="632,350 651,350 638,414 619,414" fill="var(--gold)"/>
    <text x="116" y="397" font-family="Oswald, sans-serif" font-weight="500" font-size="27" fill="var(--white)">OUR PROCESS</text>
    <rect x="690" y="380" width="9" height="9" fill="var(--navy)"/>
    <text class="brand" x="705" y="392" font-size="22">Northvale</text>

    <path class="link" d="M150 620H756"/>
    <g class="timeline-links">
      <path class="link" d="M161 572L155 610M332 572L327 610M502 572L498 610M674 572L669 610"/>
      <path class="link" d="M237 630L231 668M408 630L403 668M579 630L574 668M750 630L745 668"/>
    </g>

    <g class="timeline-steps">
      <polygon points="120,492 227,492 215,572 108,572" fill="var(--navy)"/>
      <polygon points="292,492 399,492 387,572 280,572" fill="var(--navy)"/>
      <polygon points="461,492 568,492 556,572 449,572" fill="var(--navy)"/>
      <polygon points="634,492 741,492 729,572 622,572" fill="var(--navy)"/>
      <polygon points="177,668 284,668 272,748 165,748" fill="var(--navy)"/>
      <polygon points="349,668 456,668 444,748 337,748" fill="var(--navy)"/>
      <polygon points="520,668 627,668 615,748 508,748" fill="var(--navy)"/>
      <polygon points="691,668 798,668 786,748 679,748" fill="var(--navy)"/>

      <text class="label-cond" text-anchor="middle"><tspan x="168" y="530">Transport</tspan><tspan x="168" y="552">Documents</tspan></text>
      <text class="label-cond" text-anchor="middle"><tspan x="339" y="530">Document</tspan><tspan x="339" y="552">Preparation</tspan></text>
      <text class="label-cond" text-anchor="middle"><tspan x="508" y="529">AI &amp; Data</tspan><tspan x="508" y="551">Extraction</tspan></text>
      <text class="label-cond" text-anchor="middle"><tspan x="681" y="529">Deliver</tspan><tspan x="681" y="551">Documents</tspan></text>
      <text class="label-cond" text-anchor="middle"><tspan x="224" y="706">Inventory</tspan><tspan x="224" y="728">Records</tspan></text>
      <text class="label-cond" text-anchor="middle"><tspan x="396" y="706">Scan</tspan><tspan x="396" y="728">Documents</tspan></text>
      <text class="label-cond" text-anchor="middle"><tspan x="567" y="707">Quality</tspan><tspan x="567" y="729">Control</tspan></text>
      <text class="label-cond" text-anchor="middle"><tspan x="738" y="696">Records</tspan><tspan x="738" y="717">Retention or</tspan><tspan x="738" y="738">Destruction</tspan></text>
    </g>

    <g class="timeline-tags">
      <polygon points="144,610 166,610 162,630 140,630" fill="var(--navy)"/>
      <polygon points="230,610 252,610 248,630 226,630" fill="var(--navy)"/>
      <polygon points="316,610 338,610 334,630 312,630" fill="var(--navy)"/>
      <polygon points="401,610 423,610 419,630 397,630" fill="var(--navy)"/>
      <polygon points="487,610 509,610 505,630 483,630" fill="var(--navy)"/>
      <polygon points="572,610 594,610 590,630 568,630" fill="var(--navy)"/>
      <polygon points="658,610 680,610 676,630 654,630" fill="var(--navy)"/>
      <polygon points="743,610 765,610 761,630 739,630" fill="var(--navy)"/>
      <text class="num" text-anchor="middle"><tspan x="153" y="625">1</tspan><tspan x="239" y="625">2</tspan><tspan x="325" y="625">3</tspan><tspan x="410" y="625">4</tspan><tspan x="496" y="625">5</tspan><tspan x="581" y="625">6</tspan><tspan x="667" y="625">7</tspan><tspan x="752" y="625">8</tspan></text>
    </g>

    <use href="#i-transport" x="155" y="441" width="42" height="42"/>
    <use href="#i-prep" x="327" y="440" width="42" height="42"/>
    <use href="#i-ai" x="492" y="437" width="44" height="44"/>
    <use href="#i-deliver" x="665" y="436" width="46" height="46"/>
    <use href="#i-inventory" x="196" y="755" width="42" height="42"/>
    <use href="#i-scan" x="368" y="755" width="42" height="42"/>
    <use href="#i-quality" x="540" y="755" width="46" height="46"/>
    <use href="#i-records" x="710" y="755" width="46" height="46"/>
  </g>

  <!-- ===== Panel 3: card grid ===== -->
  <g class="panel-grid">
    <rect x="31" y="908" width="842" height="572" fill="var(--panel-gray)"/>
    <rect x="398" y="962" width="9" height="9" fill="var(--navy)"/>
    <text class="brand" x="413" y="975" font-size="22">Northvale</text>

    <g class="grid-links">
      <path class="link" d="M206 1160V1203H305M371 1160V1186M539 1160V1186M705 1160V1203H606"/>
      <path class="link" d="M206 1263V1222H305M371 1240V1263M539 1240V1263M705 1263V1222H606"/>
    </g>

    <rect class="card" x="139" y="1012" width="135" height="134"/>
    <rect class="card" x="305" y="1012" width="135" height="134"/>
    <rect class="card" x="471" y="1012" width="135" height="134"/>
    <rect class="card" x="637" y="1012" width="135" height="134"/>
    <rect class="card" x="139" y="1279" width="135" height="134"/>
    <rect class="card" x="305" y="1279" width="135" height="134"/>
    <rect class="card" x="471" y="1279" width="135" height="134"/>
    <rect class="card" x="637" y="1279" width="135" height="134"/>

    <rect class="card" x="305" y="1186" width="301" height="54"/>
    <text x="456" y="1222" text-anchor="middle" font-family="Poppins, sans-serif" font-weight="500" font-size="17" fill="var(--text-dark)">OUR PROCESS</text>

    <use href="#i-transport" x="186" y="1033" width="40" height="40"/>
    <use href="#i-inventory" x="352" y="1033" width="40" height="40"/>
    <use href="#i-prep" x="518" y="1033" width="40" height="40"/>
    <use href="#i-scan" x="685" y="1033" width="40" height="40"/>
    <use href="#i-ai" x="186" y="1305" width="42" height="42"/>
    <use href="#i-quality" x="352" y="1305" width="42" height="42"/>
    <use href="#i-deliver" x="518" y="1303" width="44" height="44"/>
    <use href="#i-records" x="685" y="1303" width="42" height="42"/>

    <text class="label-card" text-anchor="middle"><tspan x="207" y="1104">Transport</tspan><tspan x="207" y="1119">Documents</tspan></text>
    <text class="label-card" text-anchor="middle"><tspan x="373" y="1104">Inventory</tspan><tspan x="373" y="1119">Records</tspan></text>
    <text class="label-card" text-anchor="middle"><tspan x="539" y="1104">Document</tspan><tspan x="539" y="1119">Preparation</tspan></text>
    <text class="label-card" text-anchor="middle"><tspan x="705" y="1104">Scan</tspan><tspan x="705" y="1119">Documents</tspan></text>
    <text class="label-card" text-anchor="middle"><tspan x="207" y="1377">AI &amp; Data</tspan><tspan x="207" y="1392">Extraction</tspan></text>
    <text class="label-card" text-anchor="middle"><tspan x="373" y="1377">Quality</tspan><tspan x="373" y="1392">Control</tspan></text>
    <text class="label-card" text-anchor="middle"><tspan x="539" y="1377">Deliver</tspan><tspan x="539" y="1392">Documents</tspan></text>
    <text class="label-card" text-anchor="middle"><tspan x="705" y="1369">Records</tspan><tspan x="705" y="1384">Retention or</tspan><tspan x="705" y="1399">Destruction</tspan></text>

    <g class="grid-tags">
      <rect class="card" x="192" y="1132" width="30" height="28"/>
      <rect class="card" x="356" y="1132" width="30" height="28"/>
      <rect class="card" x="524" y="1132" width="30" height="28"/>
      <rect class="card" x="690" y="1132" width="30" height="28"/>
      <rect class="card" x="192" y="1263" width="30" height="28"/>
      <rect class="card" x="356" y="1263" width="30" height="28"/>
      <rect class="card" x="524" y="1263" width="30" height="28"/>
      <rect class="card" x="690" y="1263" width="30" height="28"/>
      <text class="num-card" text-anchor="middle"><tspan x="207" y="1151">1</tspan><tspan x="371" y="1151">2</tspan><tspan x="539" y="1151">3</tspan><tspan x="705" y="1151">4</tspan></text>
      <text class="num-card" text-anchor="middle"><tspan x="207" y="1282">5</tspan><tspan x="371" y="1282">6</tspan><tspan x="539" y="1282">7</tspan><tspan x="705" y="1282">8</tspan></text>
    </g>
  </g>
</svg>
</div>
</div>
</body>
</html>
```